" A ORBALI Sistemas de Controle Industriais (ORBALI) é uma empresa brasileira cujo foco é o desenvolvimento de sistemas de análise e medição de processos industriais através da utilização de visão computacional. A ORBALI tem por objetivo fornecer ao mercado produtos e soluções para controle avançado e otimização de processos industriais utilizando análise de imagens. ****Os produtos e soluções da ORBALI realizam análises online de qualidade do processo industrial permitindo um controle imediato e continuo do processo industrial pelo cliente. Este é um conceito que pode também ser mostrado na site. O mercado alvo da ORBALI é o mercado industrial, em especial o mercado de mineração onde a ORBALI oferece analisadores online de processos industriais e projetos especiais para controles avançados de processos, promovendo para seus clientes melhorias nos seus processos e ganhos de produtividade. Dentro de seu plano estratégico a ORBALI tem como meta se tornar um dos principais fornecedores de soluções inovadoras de sistemas de visão computacional no mercado nacional e se tornar um exportador destas soluções para América do Sul e outros mercados internacionais. "

```html
<!DOCTYPE html>
<html lang="pt-BR">
<head>
<meta charset="utf-8">
<title>ORBALI Sistemas de Controle Industriais</title>
<link rel="stylesheet" href="https://fonts.googleapis.com/css2?family=Raleway:wght@300;400;600;700&family=Open+Sans:wght@400;600;700&display=swap">
<style>
:root{
  --green:#4caf2e;
  --green-dark:#2f8a1c;
  --green-light:#7ccc4e;
  --ink:#2a2a2a;
  --muted:#555;
  --header:#2b2b2b;
  --line:#dcdcdc;
  --photo:#c8c8c8;
  --page:#ffffff;
}
*{box-sizing:border-box;margin:0;padding:0}
html,body{width:1200px;height:1200px;overflow:hidden;background:var(--page)}
body{font-family:"Open Sans",Arial,sans-serif;color:var(--ink);position:relative}
.site-header{position:absolute;left:228px;top:0;width:744px;height:48px;background:var(--header);display:flex;align-items:center;justify-content:space-between;padding:0 14px}
.brand{display:flex;align-items:center;gap:8px;color:#fff;font-family:"Raleway",sans-serif;font-weight:700;font-size:22px;letter-spacing:1px}
.brand-dot{width:26px;height:26px;border-radius:50%;background:var(--green)}
.brand small{display:block;font-size:6px;font-weight:400;letter-spacing:.5px;color:#bbb}
.main-nav{display:flex;gap:2px}
.main-nav a{color:#fff;text-decoration:none;font-size:7.5px;font-weight:700;padding:5px 6px;text-transform:uppercase}
.main-nav a.active{background:var(--green)}
.hero{position:absolute;left:228px;top:48px;width:744px;height:290px;overflow:hidden}
.hero-photo{position:absolute;inset:0;background:linear-gradient(160deg,#8d8a83 0%,#6c6a64 35%,#4d4a44 70%,#3a3833 100%)}
.hero-circle{position:absolute;left:520px;top:16px;width:240px;height:240px;border-radius:50%;background:var(--green);border:6px solid rgba(255,255,255,.85);color:#fff;text-align:center;padding:50px 30px 0}
.hero-circle h2{font-family:"Raleway",sans-serif;font-weight:300;font-size:26px;letter-spacing:1px;margin-bottom:10px}
.hero-circle p{font-family:"Raleway",sans-serif;font-size:11.5px;line-height:1.35}
.intro{position:absolute;left:270px;top:350px;width:660px;text-align:center}
.intro h1{font-family:"Raleway",sans-serif;font-weight:400;font-size:22px;color:var(--green)}
.intro h1 strong{font-weight:700}
.intro p{margin-top:6px;font-size:10.5px;font-weight:700;line-height:1.55;color:var(--ink)}
.tabs{position:absolute;left:288px;top:480px;display:flex;gap:3px}
.tabs span{font-size:8.5px;padding:5px 12px;background:#f2f2f2;border:1px solid var(--line);color:#333}
.tabs span.active{background:var(--green);color:#fff;border-color:var(--green)}
.team{position:absolute;left:288px;top:500px;width:624px;border-top:1px solid var(--line)}
.member{display:flex;gap:12px;padding:8px 0;height:112px;border-bottom:1px solid var(--line)}
.member-photo{flex:0 0 100px;height:96px;background:var(--photo)}
.member-body h3{font-size:10px;font-weight:700;margin-bottom:4px}
.member-body p{font-size:7.5px;line-height:1.45;color:var(--muted)}
.member-body p+p{margin-top:6px}
.member-body b{color:var(--ink)}
.contact-title{position:absolute;left:290px;top:960px;font-family:"Raleway",sans-serif;font-size:26px;font-weight:700;color:var(--green-dark)}
.contact-title span{font-weight:400;color:var(--green)}
.contact-form{position:absolute;left:290px;top:1004px;width:330px}
.row{display:flex;gap:8px;margin-bottom:8px}
.field{flex:1;height:18px;border:1px solid #bbb;font-size:6.5px;color:#888;padding:3px 5px}
.field.area{height:62px}
.send{display:inline-block;background:var(--green);color:#fff;font-size:8px;font-weight:700;padding:4px 16px}
.contact-info{position:absolute;left:640px;top:1012px;width:280px;display:flex;justify-content:space-between;text-align:center;font-size:7px;line-height:1.4;color:var(--muted)}
.contact-info svg{display:block;margin:0 auto 4px}
.footer-band{position:absolute;left:0;top:1132px;width:1200px;height:14px;background:linear-gradient(180deg,#b7e49a,var(--green-light))}
.site-footer{position:absolute;left:0;top:1146px;width:1200px;height:54px;background:var(--green);color:#fff;text-align:center;padding-top:10px}
.site-footer nav{display:flex;justify-content:center;gap:14px;font-size:7.5px;font-weight:700;text-transform:uppercase}
.site-footer p{margin-top:10px;font-size:7.5px}
</style>
</head>
<body>
<header class="site-header">
  <div class="brand"><span class="brand-dot"></span><div>ORBALI<small>SISTEMAS DE CONTROLE INDUSTRIAIS</small></div></div>
  <nav class="main-nav">
    <a href="#">Home</a><a href="#" class="active">A Empresa</a><a href="#">Tecnologia</a><a href="#">Produtos e Serviços</a><a href="#">Clientes e Parceiros</a><a href="#">Contato</a>
  </nav>
</header>

<section class="hero">
  <div class="hero-photo" role="img" aria-label="Engenheiros com capacete e colete de segurança observando uma área de mineração"></div>
  <div class="hero-circle">
    <h2>SOBRE NÓS...</h2>
    <p>Somos uma empresa de tecnologia com foco no desenvolvimento de sistemas de análise e medição online de processos industriais através da utilização de visão computacional.</p>
  </div>
</section>

<section class="intro">
  <h1>Otimizar o processo para <strong>gerar valor</strong> e <strong>resultados</strong> !</h1>
  <p>Nosso objetivo é atender o mercado com produtos e soluções inovadoras para melhoria da qualidade e geração de ganhos reais de produtividade dos processos de nossos clientes através de sistemas de medição e análise avançada, analisadores online de processos e otimização de plantas industriais utilizando análise de imagens.</p>
</section>

<div class="tabs"><span>ORBALI</span><span>Visão, missão &amp; valores</span><span class="active">Quem Somos</span></div>

<section class="team">
  <article class="member">
    <div class="member-photo" role="img" aria-label="Foto de Márcio Teles Andrade"></div>
    <div class="member-body">
      <h3>Márcio Teles Andrade</h3>
      <p>Engenheiro com 15 anos de experiência em eletrônica, desenvolvimento de produtos, instrumentação e automação. Atuou em projetos de controle de processos industriais, implantação de sistemas de medição online e gestão de equipes técnicas em mineração.</p>
      <p><b>Áreas de Atuação:</b> Engenharia Elétrica, Especialidade Circuitos Eletrônicos; Engenharia de Controle e Automação, Especialidade Instrumentação Industrial; Processamento de Sinais e Imagens.</p>
    </div>
  </article>
  <article class="member">
    <div class="member-photo" role="img" aria-label="Foto de Caio Ramos de Lima"></div>
    <div class="member-body">
      <h3>Caio Ramos de Lima</h3>
      <p>Doutor em visão computacional com atuação em projetos de análise de imagens aplicados à indústria. Coordenou o desenvolvimento de analisadores online e publicou trabalhos sobre medição de partículas e controle avançado de processos.</p>
      <p><b>Áreas de Atuação:</b> Visão Computacional; Processamento Digital de Imagens; Reconhecimento de Padrões; Modelagem e Otimização de Processos Minerais.</p>
    </div>
  </article>
  <article class="member">
    <div class="member-photo" role="img" aria-label="Foto de Hélio Aragão Pires Nogueira"></div>
    <div class="member-body">
      <h3>Hélio Aragão Pires Nogueira</h3>
      <p>Engenheiro de produção com experiência em gestão de projetos, planejamento industrial e implantação de soluções de automação em usinas de beneficiamento. Responsável pelo relacionamento com clientes e parceiros.</p>
      <p><b>Áreas de Atuação:</b> Gestão de Projetos; Engenharia de Produção; Planejamento e Controle da Produção; Desenvolvimento de Novos Negócios.</p>
    </div>
  </article>
  <article class="member">
    <div class="member-photo" role="img" aria-label="Foto de Rogério Calixto Mendes"></div>
    <div class="member-body">
      <h3>Rogério Calixto Mendes</h3>
      <p>Especialista em tecnologia da informação com atuação em desenvolvimento de software industrial, bancos de dados e integração de sistemas. Participou de projetos de supervisão e rastreabilidade em grandes empresas do setor mineral.</p>
      <p><b>Áreas de Atuação:</b> Engenharia de Software; Sistemas Supervisórios; Integração de Dados Industriais; Infraestrutura de Redes.</p>
    </div>
  </article>
</section>

<h2 class="contact-title">Fale conosco <span>agora mesmo !</span></h2>

<form class="contact-form">
  <div class="row"><div class="field">Digite seu nome</div><div class="field">Digite seu email</div></div>
  <div class="row"><div class="field area">Digite sua mensagem</div></div>
  <span class="send">Enviar</span>
</form>

<div class="contact-info">
  <div>
    <svg width="16" height="16" viewBox="0 0 16 16"><path d="M8 1a5 5 0 0 0-5 5c0 4 5 9 5 9s5-5 5-9a5 5 0 0 0-5-5z" fill="#555"/><circle cx="8" cy="6" r="2" fill="#fff"/></svg>
    Rua das Acácias 240<br>Bairro Jardim Norte<br>CEP 31.555-100<br>Belo Horizonte - MG
  </div>
  <div>
    <svg width="16" height="16" viewBox="0 0 16 16"><path d="M4 1h3l1 4-2 1a8 8 0 0 0 4 4l1-2 4 1v3c0 1-1 2-2 2C7 14 2 9 2 3c0-1 1-2 2-2z" fill="#555"/></svg>
    (31) 3555-0142<br>(31) 99555-0187
  </div>
  <div>
    <svg width="16" height="16" viewBox="0 0 16 16"><rect x="1" y="3" width="14" height="10" fill="#555"/><path d="M1 3l7 6 7-6" stroke="#fff" fill="none"/></svg>
    contato@orbali.com.br
  </div>
</div>

<div class="footer-band"></div>
<footer class="site-footer">
  <nav><span>Home</span><span>A Empresa</span><span>Tecnologia</span><span>Produtos e Serviços</span><span>Clientes e Parceiros</span><span>Contato</span></nav>
  <p>© todos os direitos reservados ORBALI</p>
</footer>
</body>
</html>
```